Brightmold Laser Lipo Brochure

Need a 3 panel brochure
Full Colour
Sales/info brochure
Photos provided
Testimonials
Product Specs - http://brightmoldcontour.com/brightmoldcontour/request-a-demo/opportunity.aspx
Brightmold Laser Lipo is trademarked
Website and contact details
description of what about the technique-
http://brightmoldcontour.com/brightmoldcontour/laser-lipo.aspx
Examples of successful clinics - to follow

Also require business card to compliment the brochure

Target Market(s)

Target Audience Clinics, Gyms, Salons

Industry/Entity Type

Business

Requirements
Must have
• website www.brightmoldcontour.com
testimonials
"After just two laser-lipo sessions I was happily surprised to find that I had dropped between one and two belt sizes ..... tablequill.com.au TKM"
"I have been a number of the laser lipo treatments and using the VNA cream in between session with great results. Have lost 4cm around waist. Highly recommend.....tablequill.com.au MarnieS"

```html
<!DOCTYPE html>
<html lang="en">
<head>
<meta charset="utf-8">
<title>Brightmold Laser Lipo – Brochure</title>
<link href="https://fonts.googleapis.com/css2?family=Arimo:wght@400;700&family=Tinos:ital,wght@0,400;0,700;1,700&display=swap" rel="stylesheet">
<style>
:root{
  --navy:#0c3563;
  --blue:#1d5e9c;
  --sky:#3f8fd0;
  --pale:#9cc8ec;
  --ink:#1d1d1d;
  --paper:#ffffff;
  --stage-top:#f4f4f4;
  --stage-bottom:#0a0a0a;
  --offer-red:#d8202a;
  --tray:#dcdde0;
}
*{margin:0;padding:0;box-sizing:border-box}
html,body{width:1147px;height:1200px;overflow:hidden}
body{
  position:relative;
  background:linear-gradient(160deg,var(--stage-top) 0%,#b9b9b9 45%,#6d6d6d 75%,var(--stage-bottom) 100%);
  font-family:"Arimo",Arial,sans-serif;color:var(--ink);
}
.spread{position:absolute;display:flex;box-shadow:4px 6px 10px rgba(0,0,0,.45)}
.spread--outer{left:63px;top:70px;width:995px;height:470px}
.spread--inner{left:68px;top:652px;width:995px;height:468px}
.panel{position:relative;width:332px;height:100%;background:var(--paper);overflow:hidden;
  border-right:1px solid #c8d6e4}
.panel:last-child{border-right:none}
.panel__header{position:absolute;left:0;top:0;right:0;height:34px;
  background:linear-gradient(90deg,var(--navy) 0%,var(--blue) 35%,var(--blue) 75%,var(--sky) 100%);
  font-family:"Tinos",serif;font-weight:700;color:#fff;font-size:12px;padding:11px 0 0 34px}
.panel__footer{position:absolute;left:0;bottom:0;right:0;height:30px;
  background:linear-gradient(90deg,var(--navy),var(--blue) 40%,var(--sky) 80%,var(--navy));
  font-family:"Tinos",serif;font-style:italic;font-weight:700;color:#fff;font-size:11px;
  text-align:center;padding-top:8px}
.panel__edge{position:absolute;left:0;top:34px;bottom:30px;width:18px;
  background:linear-gradient(90deg,var(--navy),var(--sky))}
.photo{position:absolute}
.small{position:absolute;font-size:7px;line-height:1.35}
.small p{margin-bottom:8px}

.contact-card{position:absolute;left:81px;top:361px;width:192px;height:65px;border-radius:6px;
  background:linear-gradient(160deg,var(--sky),var(--navy));box-shadow:2px 3px 5px rgba(0,0,0,.4);
  color:#dce9f6;font-size:7px;line-height:1.35;padding:8px 0 0 41px;border:1px solid #cfe0f0}

.brand{position:absolute;left:100px;top:50px;font-family:"Tinos",serif;font-size:30px;color:#222}
.brand__sub{position:absolute;left:180px;top:86px;font-size:10px;color:#333}
.brand__tag{position:absolute;left:100px;top:101px;font-size:7px;font-style:italic;color:#333}
.claims{position:absolute;right:66px;top:126px;text-align:right;font-size:9.5px;line-height:1.3;color:#333;font-style:italic}
.snap{position:absolute;background:#fff;box-shadow:1px 2px 4px rgba(0,0,0,.5);padding:4px 4px 0}
.snap__label{font-family:"Arimo",sans-serif;font-weight:700;font-size:14px;color:#111;text-align:center}
.offer{position:absolute;left:90px;top:333px;width:146px;text-align:center;line-height:1}
.offer__price{font-size:12px;color:var(--blue);font-style:italic;font-weight:700}
.offer__title{font-size:12px;color:var(--offer-red);font-weight:700}
.offer__note{font-size:7px;color:var(--blue);font-style:italic;font-weight:700}
.sites{position:absolute;top:369px;font-size:6px;color:#555}

.panel--cover{background:linear-gradient(180deg,var(--navy) 0%,var(--blue) 60%,var(--sky) 100%)}
.cover__title{position:absolute;left:43px;top:16px;font-family:"Tinos",serif;font-weight:700;color:#fff;
  font-size:25px;line-height:32px;text-shadow:1px 1px 2px rgba(0,0,0,.4)}
.cover__lede{position:absolute;left:160px;top:78px;font-family:"Tinos",serif;font-style:italic;font-weight:700;
  color:#fff;font-size:10px;line-height:1.35}
.quote{position:absolute;font-family:"Tinos",serif;font-weight:700;color:#fff;font-size:7.5px;line-height:1.3}

.tab{position:absolute;left:2px;height:23px;background:linear-gradient(90deg,var(--navy),var(--blue));
  color:#fff;font-family:"Tinos",serif;font-size:13px;padding:3px 12px 0 30px;
  box-shadow:2px 2px 3px rgba(0,0,0,.35)}
.body-copy{position:absolute;font-size:7px;line-height:1.38}
.body-copy p{text-indent:20px}
.bullets{position:absolute;font-size:7px;line-height:1.36;list-style:none}
.bullets li::before{content:"•";display:inline-block;width:22px}
.tray{position:absolute;left:20px;top:129px;width:298px;height:222px;background:var(--tray)}
.card{position:absolute;width:64px;height:82px;background:#fff;box-shadow:1px 1px 3px rgba(0,0,0,.35);padding:3px}
.card__img{width:58px;height:60px}
.card__label{font-size:10px;text-align:center;color:#111}
.specs{position:absolute;left:30px;top:96px;font-size:7px;line-height:1.36;width:285px}
.specs p{margin-bottom:9px}
</style>
</head>
<body>

<section class="spread spread--outer">
  <article class="panel">
    <div class="panel__header">Brightmold Laser Lipo</div>
    <div class="panel__edge"></div>
    <svg class="photo" style="left:61px;top:74px" width="210" height="144" role="img" aria-label="Photo of a woman in white stretching a scarf on a beach">
      <defs><linearGradient id="beach" x1="0" y1="0" x2="0" y2="1"><stop offset="0" stop-color="#e9f2f7"/><stop offset=".55" stop-color="#7fc3d6"/><stop offset="1" stop-color="#3d9bb5"/></linearGradient></defs>
      <rect width="210" height="144" fill="url(#beach)"/>
    </svg>
    <div class="small" style="left:32px;top:239px;width:282px">
      <p>We are currently operating two machines with one technician working two treatment rooms and treat 24 clients per day - we are open 6 hours and allow 30 mins per client.</p>
      <p>Our current promotion sold 350 courses of between 2 and 6 treatments.</p>
      <p>Before and after images on this site are our own images and have been taken at 2 - 7 treatment intervals.</p>
      <p>Cm loss per client averages from 1 - 4cm per treatment.</p>
      <p>Clients are required to drink 3 ltrs of water per day min during treatments and do a min of 30mins exersize per day also.</p>
    </div>
    <div class="contact-card">
      Nadia's Brightmold<br>14c Harbour View Rd - Side Entrance<br>Larkwhistle 6999<br>0400 555 218<br>nadia@brightmoldcontour.com
    </div>
    <div class="panel__footer">www.brightmoldcontour.com</div>
  </article>

  <article class="panel">
    <div class="panel__header">Brightmold Laser Lipo</div>
    <div class="brand">Brightmold</div>
    <div class="brand__sub">laser lipo</div>
    <div class="brand__tag">"Now you can keep it off forever!"</div>
    <div class="claims">PAIN FREE<br>Non Invasive<br>Lose cm's in minutes</div>
    <svg class="photo" style="left:42px;top:128px" width="235" height="252" role="img" aria-label="Slim waist with tape measure above a blue swoosh background">
      <defs><linearGradient id="swoosh" x1="0" y1="0" x2="1" y2="1"><stop offset="0" stop-color="#e8f1f9"/><stop offset=".6" stop-color="#4f97d2"/><stop offset="1" stop-color="#1b5c9c"/></linearGradient></defs>
      <path d="M0 150 Q60 210 235 190 L235 252 L40 252 Q10 210 0 150Z" fill="url(#swoosh)"/>
      <rect x="0" y="0" width="104" height="80" fill="#e7c9b4"/>
    </svg>
    <div class="snap" style="left:56px;top:204px;width:104px;height:125px;transform:rotate(-6deg)">
      <svg width="96" height="96" role="img" aria-label="Before photo of a midriff"><rect width="96" height="96" fill="#c98e80"/></svg>
      <div class="snap__label">Before</div>
    </div>
    <div class="snap" style="left:163px;top:172px;width:104px;height:125px;transform:rotate(4deg)">
      <svg width="96" height="96" role="img" aria-label="After photo of a midriff"><rect width="96" height="96" fill="#d09a8a"/></svg>
      <div class="snap__label">After</div>
    </div>
    <div class="offer">
      <div class="offer__price">$99 Treatment</div>
      <div class="offer__title">Introductory Offer</div>
      <div class="offer__note">For a Limited Time Only</div>
    </div>
    <svg class="photo" style="left:234px;top:311px" width="28" height="24" aria-hidden="true"><rect width="28" height="24" rx="4" fill="var(--offer-red)"/></svg>
    <div class="sites" style="left:89px">brightmoldcontour.com</div>
    <div class="sites" style="left:160px">glowhavenbeauty.com.au</div>
    <div class="panel__footer">www.brightmoldcontour.com</div>
  </article>

  <article class="panel panel--cover">
    <div class="cover__title">Brightmold<br>Laser<br>Lipo</div>
    <div class="cover__lede">Revolutionary procedure for<br>instant and permanent cm-loss</div>
    <svg class="photo" style="left:0;top:127px" width="125" height="163" role="img" aria-label="Photo of women exercising at a gym"><rect width="125" height="163" fill="#b9a08f"/></svg>
    <svg class="photo" style="left:125px;top:127px" width="206" height="121" role="img" aria-label="Photo of a slim waist in white underwear"><rect width="206" height="121" fill="#eee3dc"/></svg>
    <div class="quote" style="left:146px;top:254px;width:165px">After just two laser-lipo sessions I was happily surprised to find that I had dropped between one and two belt sizes ..... tablequill.com.au TKM</div>
    <div class="quote" style="left:10px;top:307px;width:110px">I have been a number of the laser lipo treatments and using the VNA cream in between session with great results. Have lost 4cm around waist. Highly recommend.....tablequill.com.au MarnieS</div>
    <svg class="photo" style="left:125px;top:291px" width="206" height="101" role="img" aria-label="Photo of a waist wrapped with a tape measure"><rect width="206" height="101" fill="#e2c6b4"/></svg>
    <div class="panel__footer" style="background:linear-gradient(90deg,var(--blue),var(--sky));padding-top:9px">www.brightmoldcontour.com</div>
  </article>
</section>

<section class="spread spread--inner">
  <article class="panel">
    <div class="panel__header">Brightmold Laser Lipo</div>
    <div class="panel__edge"></div>
    <div class="tab" style="top:62px">Laser Lipo</div>
    <div class="body-copy" style="left:35px;top:92px;width:287px">
      <p>Brightmold Laser Lipo is a revolutionary procedure for instant and permanent cm-loss. It works by cellulite removal and fat reduction which in turn leads to skin tightening using state of the art laser technology. Lasers simply 'melt' the fat in the desired area and it is then expelled from the body naturally through normal metabolism.</p>
      <p>The treatment is a quick, non-invasive and permanent solution to stubborn fat. To achieve the desired result a course of 6 - 8 treatments is usually required, however clients are seeing great results over a few treatments.</p>
      <p>Before the commencement of treatments a full appraisal of your individual requirements is established, with measurements and photographs. You can then have a discounted trial treatment - from which you will begin to see immediate results.</p>
      <p>Each treatment takes no more than 15 minutes so you could even pop down during your lunch hour!</p>
      <p>Using up to eight low-level intelligent laser pads, with 32 diode lasers per pad - you can now achieve better results than machines used by other clinics over an increased target area of the body.</p>
    </div>
    <div class="tab" style="top:245px">Treatment Areas Include</div>
    <ul class="bullets" style="left:35px;top:275px">
      <li>Stomach</li><li>Hips</li><li>Thighs</li><li>Back Fat</li><li>Arms</li><li>Double Chin</li><li>Mummy Tummy</li><li>Man Boobs</li>
    </ul>
    <div class="tab" style="top:362px">Brightmold Laser Lipo Applications Include</div>
    <ul class="bullets" style="left:37px;top:394px">
      <li>Instant &amp; Permanent Inch Loss</li><li>Skin Tightening</li><li>Dramatically Reduces Cellulite</li>
    </ul>
    <div class="panel__footer">www.brightmoldcontour.com</div>
  </article>

  <article class="panel">
    <div class="panel__header">Brightmold Laser Lipo</div>
    <div class="panel__edge"></div>
    <div class="tab" style="top:61px">Benefits Of Brightmold Laser Lipo</div>
    <div class="body-copy" style="left:30px;top:92px;width:280px">There are many benefits to Brightmold laser lipo over traditional forms of liposuction. It is safe, non-invasive and you have no need for recovery. Also there is no pain, no needles, no starvation diets and there are no negative side effects.</div>
    <div class="tray">
      <div class="card" style="left:24px;top:23px"><svg class="card__img" role="img" aria-label="After photo of a torso"><rect width="58" height="60" fill="#c99b86"/></svg><div class="card__label">after</div></div>
      <div class="card" style="left:117px;top:23px"><svg class="card__img" role="img" aria-label="Before photo of a torso"><rect width="58" height="60" fill="#b98a74"/></svg><div class="card__label">before</div></div>
      <div class="card" style="left:212px;top:23px"><svg class="card__img" role="img" aria-label="Before photo of a torso"><rect width="58" height="60" fill="#a87c6c"/></svg><div class="card__label">before</div></div>
      <div class="card" style="left:24px;top:119px"><svg class="card__img" role="img" aria-label="Before photo of a torso"><rect width="58" height="60" fill="#c09682"/></svg><div class="card__label">before</div></div>
      <div class="card" style="left:117px;top:119px"><svg class="card__img" role="img" aria-label="After photo of a torso"><rect width="58" height="60" fill="#b38876"/></svg><div class="card__label">after</div></div>
      <div class="card" style="left:212px;top:119px"><svg class="card__img" role="img" aria-label="After photo of a torso"><rect width="58" height="60" fill="#8f7a72"/></svg><div class="card__label">after</div></div>
    </div>
    <div class="panel__footer">www.brightmoldcontour.com</div>
  </article>

  <article class="panel">
    <div class="panel__header">Brightmold Laser Lipo</div>
    <div class="panel__edge"></div>
    <div class="tab" style="top:64px">Opportunity</div>
    <div class="specs">
      <p>Technical Specifications of the Brightmold Laser Lipo</p>
      <p>8 Large pads<br>4 Small pads</p>
      <p>32 Diodes on each large pad - 16 x 650nm and 16 x 940nm<br>4 Diodes on each small pad - 2 x 650nm and 2 x 940nm</p>
      <p>272 Diodes in total.</p>
      <p>650nm targets fat<br>940nm targets cellulite</p>
      <p>Each system comes with 8 hours onsite training for 2<br>Literature x 200 promotional flyers<br>Posters<br>1 x promotional poster<br>1x measurement poster - for before and after pictures</p>
      <p>12 months warranty</p>
      <p>Salon/Clinic promotion on brightmoldcontour.com website<br>Promotional and marketing support</p>
      <p>Currently suggested retail is aprox $250 per session per treatment area.</p>
      <p>Treatments take 20 - 30 mins</p>
      <p>With promotional specials at $99.00 per treatment</p>
      <p>Clinic open 8 hours 6 days per week with 1 technician managing one Brightmold laser lipo machine</p>
      <p>Up to 24 clients per day and 144 clients per week at $99.00 per treatment = $14256 per week</p>
    </div>
    <div class="panel__footer">www.brightmoldcontour.com</div>
  </article>
</section>

</body>
</html>
```